Metal Fabrication Business Cards

We need a business card for our business of Metal Fabrication/Welding. Our company is called "Hadley's Metal Fabrication"

We are a metal fabrication business which takes on "high class" clients- dealing with some of the biggest builders in Australia. Our work is neat, and the type of work we do is 2nd to none for quality. We want to show that on our cards. However, we would love to show a side that is down to earth and a bit more modern and contemporary - we are all young in business so would love to show that side - rather than a boring "very straight looking" card. We always have a clean workshop and take pride in our presentation. We want to come across like we are very rich, but would love to go for a surf as well! A card that basically says we have high class and will charge you a high rate - but the quality will be outstanding.

Front of card: - Simply but sharp!
-Thinking maybe white card - with nice black writing.
-On the right hand side of card a person welding - or holding a welder.
- My business name - Hadley's Metal Fabrication
-Also maybe my name - which is 'Corey" (if it doesn't work, we can put this on the back of card.)
- if needed to look better - we can put keywords on front of card like "metal fabrication, sheet metal, welding etc" but I dont want it to be crowded.

Back of card: - Also make smart but sharp!
Put details such as:
04387 21 914
hadley.fabrication@tinmailbox.com.au
7/32 Keel Street
North Tarrow QLD 4812
www.korvinfabrication.com.au
ABN 72 615 803 914

thats just an idea - its now up to you. I don't mind what you come up with - as long as it stands out from the rest and looks sharp, professional but contemporary.

Business

Put details such as:
04387 21 914
7/32 Keel Street
North Tarrow QLD 4812
ABN 72 615 803 914

Hadley's Metal Fabrication

```html
<!DOCTYPE html>
<html lang="en">
<head>
<meta charset="utf-8">
<title>Hadley's Metal Fabrication – Business Cards</title>
<link rel="stylesheet" href="https://fonts.googleapis.com/css2?family=Open+Sans:wght@300;400;600;700&display=swap">
<style>
  :root {
    --backdrop: #3b3531;
    --card: #111111;
    --card-edge: #1c1c1c;
    --orange: #f7941d;
    --silver: #d9d9d9;
    --text-light: #c9c9c9;
  }
  * { margin: 0; padding: 0; box-sizing: border-box; }
  html, body {
    width: 1200px;
    height: 900px;
    overflow: hidden;
    background: var(--backdrop);
    font-family: "Open Sans", Arial, sans-serif;
  }
  .canvas {
    position: relative;
    width: 1200px;
    height: 900px;
  }
  .card {
    position: absolute;
    top: 307px;
    width: 500px;
    height: 286px;
    background: var(--card);
    border: 1px solid var(--card-edge);
    box-shadow: 0 14px 30px rgba(0, 0, 0, 0.45);
  }
  .card--back { left: 60px; }
  .card--front { left: 640px; }

  /* Back: vertical business name */
  .back-name {
    position: absolute;
    left: 20px;
    top: 0;
    width: 160px;
    height: 286px;
    display: flex;
    align-items: center;
    justify-content: center;
  }
  .back-name__text {
    transform: rotate(-90deg);
    white-space: nowrap;
    color: var(--orange);
    font-weight: 400;
    font-size: 30px;
    letter-spacing: 1px;
    text-align: center;
    line-height: 1.1;
  }
  .back-name__sub {
    display: block;
    font-size: 11px;
    letter-spacing: 2px;
    text-transform: uppercase;
  }

  /* Back: contact details */
  .details {
    position: absolute;
    left: 200px;
    top: 52px;
    right: 20px;
    color: var(--text-light);
    font-size: 12.5px;
    line-height: 1.55;
  }
  .details__name {
    color: var(--orange);
    font-weight: 700;
    font-size: 17px;
    letter-spacing: 0.5px;
    margin-bottom: 6px;
  }
  .contact-list { list-style: none; }
  .contact-list li {
    display: flex;
    align-items: center;
    gap: 8px;
    white-space: nowrap;
  }
  .contact-list svg { width: 11px; height: 11px; flex: none; fill: var(--orange); }
  .details__abn { margin-top: 22px; }
  .details__abn-label { color: var(--orange); }
  .details__address { margin-top: 12px; }

  /* Front: business name */
  .front-name {
    position: absolute;
    inset: 0;
    display: flex;
    flex-direction: column;
    align-items: center;
    justify-content: center;
    color: var(--silver);
    font-weight: 300;
  }
  .front-name__title {
    font-size: 46px;
    letter-spacing: 2px;
    text-transform: uppercase;
  }
  .front-name__sub {
    font-size: 14px;
    letter-spacing: 3px;
    text-transform: uppercase;
    margin-top: 2px;
    font-weight: 400;
  }
</style>
</head>
<body>
<main class="canvas">

  <section class="card card--back" aria-label="Card back">
    <div class="back-name">
      <p class="back-name__text">HADLEY'S<span class="back-name__sub">Metal Fabrication</span></p>
    </div>

    <div class="details">
      <p class="details__name">COREY</p>
      <ul class="contact-list">
        <li>
          <svg viewBox="0 0 12 12" aria-hidden="true"><path d="M2.5 1 4.3 1 5.2 3.4 4 4.3C4.6 5.7 6.3 7.4 7.7 8L8.6 6.8 11 7.7 11 9.5C11 10.3 10.3 11 9.5 11 5 10.7 1.3 7 1 2.5 1 1.7 1.7 1 2.5 1Z"/></svg>
          04387 21 914
        </li>
        <li>
          <svg viewBox="0 0 12 12" aria-hidden="true"><path d="M1 2.5H11V9.5H1Z M1.6 3 6 6.3 10.4 3" stroke="#111" stroke-width="0.8"/></svg>
          hadley.fabrication@tinmailbox.com.au
        </li>
        <li>
          <svg viewBox="0 0 12 12" aria-hidden="true"><circle cx="6" cy="6" r="5"/><path d="M1 6H11M6 1C3.8 3.5 3.8 8.5 6 11M6 1C8.2 3.5 8.2 8.5 6 11" stroke="#111" stroke-width="0.8" fill="none"/></svg>
          www.korvinfabrication.com.au
        </li>
      </ul>
      <p class="details__abn"><span class="details__abn-label">ABN:</span> 72 615 803 914</p>
      <p class="details__address">7/32 Keel Street<br>North Tarrow QLD 4812</p>
    </div>
  </section>

  <section class="card card--front" aria-label="Card front">
    <div class="front-name">
      <p class="front-name__title">Hadley's</p>
      <p class="front-name__sub">Metal Fabrication</p>
    </div>
  </section>

</main>
</body>
</html>
```